Independent Midwife for a positive birth experience needs a vibrant, and elegant business card/logo

I need a business card design with a logo. The logo I would like to be able to use on my website (www.midwifemarisol.com) next to my name.
Therefore the design of the card and logo should suit the colours and design of the website. The title of the website and company is "Marisol Quenby Fairhurst, Midwife" but I'd like to have the business card title to be "Marisol Quenby Fairhurst - Independent Midwife" in bold letters, same script font as in my website.

I provide gold standard midwifery services, one-to-one tailored care, continuity of care throughout the entire pregnancy (antenatal care), the birth and after the birth (postnatal care), home birth, water birth, breast-feeding support, and birth preparation workshops. I also am certified and offer complementary therapies: pregnancy reflexology, rebozo techniques for optimal baby positioning.

The design should incorporate similar colours and style as the website and the "Marisol Quenby Fairhurst - Independent Midwife" on the card should include the same font as in the title of the website, however, in bold. The front of the card should have a logo, title and contact information (phone number 072639518, email marisol.fairhurst@lovantamail.com, website address www.midwifemarisol.com).
The back of the card to include the services I offer.

The logo: use of colour purple (varying shades), should communicate communicate warmth, kindness, compassion. It should convey that I'm a midwife who believes in fostering a trusting relationship with my clients and to provide them with a positive pregnancy and birth experience.

Target Market(s)

Pregnant women or women who are looking to book a private midwife for better birth experience and outcome

Industry/Entity Type

Baby

Contact Information for Business Card

Name and Title on front side together with contact details
The reverse side should have services/packages offered

Font styles to use
Script
Other font styles liked:
• similar script as in my website for name and title, and easy to read font for the rest of the words

Colors
b768aa
a54599
d2a4cc
ffffff

Requirements
Must have
• same font as title of website, but slightly bolder.
• similar design, colours, patterns as in website.
• Also include a gold accent colour somewhere in the design please.
Nice to have
• perhaps a logo of pregnant belly in profile or newborn baby icon

```html
<!DOCTYPE html>
<html lang="en">
<head>
<meta charset="utf-8">
<title>Marisol Quenby Fairhurst – Independent Midwife – Business Card</title>
<link rel="stylesheet" href="https://fonts.googleapis.com/css2?family=Courgette&family=Open+Sans:wght@400;600&display=swap">
<style>
  :root {
    --stage: #000000;
    --plum: #a54599;
    --orchid: #b768aa;
    --orchid-light: #d2a4cc;
    --charcoal: #333133;
    --paper: #f0f0f2;
    --white: #ffffff;
    --ink-grey: #6b6b6b;
    --script: "Courgette", cursive;
    --sans: "Open Sans", Arial, sans-serif;
  }
  * { box-sizing: border-box; margin: 0; padding: 0; }
  html, body { width: 1200px; height: 900px; overflow: hidden; background: var(--stage); }
  .canvas {
    width: 1200px; height: 900px;
    display: flex; align-items: center; justify-content: center; gap: 40px;
  }
  .card { position: relative; width: 540px; height: 324px; overflow: hidden; }

  /* Front */
  .card-front .panels { position: absolute; inset: 0; }
  .brand-mark {
    position: absolute; left: 56px; top: 146px; width: 130px;
    text-align: center; font-family: var(--sans); font-weight: 600;
    font-size: 13px; line-height: 1.3; color: var(--plum);
  }
  .client-tag {
    position: absolute; right: 26px; top: 38px; text-align: right;
    font-family: var(--sans); color: var(--white);
  }
  .client-tag .client-name { font-size: 17px; letter-spacing: .5px; }
  .client-tag .client-role { font-size: 11px; color: #cfcfcf; }

  .contact-item { position: absolute; right: 18px; white-space: nowrap; text-align: right; }
  .contact-title { top: 194px; font-family: var(--script); font-size: 11px; color: var(--plum); }
  .contact-line { font-family: var(--sans); font-size: 11px; color: var(--ink-grey); }
  .contact-phone { top: 220px; right: 52px; }
  .contact-email { top: 254px; }
  .contact-web { top: 270px; }
  .rule {
    position: absolute; right: 18px; height: 1px; width: 220px;
    background: linear-gradient(to left, var(--plum), rgba(165,69,153,0));
  }
  .rule-top { top: 214px; }
  .rule-bottom { top: 246px; }
  .icon { position: absolute; right: 18px; width: 26px; height: 26px; }
  .icon-phone { top: 166px; }
  .icon-web { top: 218px; }

  /* Back */
  .card-back .upper { position: absolute; left: 0; top: 0; width: 100%; height: 200px; background: var(--charcoal); }
  .card-back .lower { position: absolute; left: 0; top: 200px; width: 100%; height: 124px; background: var(--plum); }
  .card-back .brand-mark-back {
    position: absolute; left: 0; right: 0; top: 88px; text-align: center;
    font-family: var(--sans); font-weight: 600; font-size: 16px; color: var(--orchid);
  }
  .card-back .title {
    position: absolute; left: 0; right: 0; top: 234px; text-align: center;
    font-family: var(--script); font-size: 16px; color: var(--white);
  }
</style>
</head>
<body>
<main class="canvas">

  <section class="card card-front" aria-label="Business card front">
    <svg class="panels" viewBox="0 0 540 324" width="540" height="324" aria-hidden="true">
      <rect width="540" height="324" fill="var(--white)"/>
      <polygon points="0,0 160,0 258,150 206,324 0,324" fill="var(--plum)"/>
      <polygon points="174,0 540,0 540,92 266,146" fill="var(--charcoal)"/>
      <polygon points="272,156 540,104 540,324 218,324" fill="var(--paper)"/>
      <polygon points="121,88 196,140 170,214 72,214 46,140" fill="var(--white)"/>
    </svg>
    <div class="brand-mark">Marisol Quenby<br>Fairhurst</div>

    <div class="client-tag">
      <div class="client-name">CLIENT NAME</div>
      <div class="client-role">Destination</div>
    </div>

    <svg class="icon icon-phone" viewBox="0 0 26 26" aria-hidden="true">
      <polygon points="7,1 19,1 25,13 19,25 7,25 1,13" fill="var(--plum)"/>
      <path d="M7 10c0-2 2-3 6-3s6 1 6 3v1h-3v-1.5h-6V11H7z M9 13h8l1 5H8z" fill="var(--white)"/>
    </svg>
    <div class="contact-item contact-title">Marisol Quenby Fairhurst - Independent Midwife</div>
    <div class="rule rule-top"></div>
    <div class="contact-item contact-line contact-phone">072639518</div>
    <svg class="icon icon-web" viewBox="0 0 26 26" aria-hidden="true">
      <polygon points="7,1 19,1 25,13 19,25 7,25 1,13" fill="var(--plum)"/>
      <rect x="7" y="8" width="12" height="8" fill="var(--white)"/>
      <rect x="9" y="10" width="8" height="4" fill="var(--plum)"/>
      <rect x="11" y="17" width="4" height="2" fill="var(--white)"/>
    </svg>
    <div class="rule rule-bottom"></div>
    <div class="contact-item contact-line contact-email">marisol.fairhurst@lovantamail.com</div>
    <div class="contact-item contact-line contact-web">www.midwifemarisol.com</div>
  </section>

  <section class="card card-back" aria-label="Business card back">
    <div class="upper"></div>
    <div class="lower"></div>
    <div class="brand-mark-back">Marisol Quenby Fairhurst</div>
    <div class="title">Marisol Quenby Fairhurst - Independent Midwife</div>
  </section>

</main>
</body>
</html>
```